Web design for a Senior Home Care company

I want a web design for a home care company called Larkmoor Home Care. What LHC does is send caregivers into people's homes to assist with daily living needs such as companionship, food preparation, cleaning, bathing, using the bathroom, etc. Most of the clients are seniors. The people deciding to use LHC are usually the 50 year old children of these senior citizens. Most visitors to the site will be women searching for this service for their parents.

The call to action is to inspire the website visitors to call us to set up an appointment to meet them in their home. The site design should inspire confidence in Larkmoor Home Care to care for people's needs. We want to show the same attributes that a parent should have. Safety, Security and Loving Care.

Again, the goal of the site is to inspire and make it EASY for visitors to contact us either by phone call or through the website. The first choice is that they call us.

To help you with your ideas, In the attachments I've included different versions of our logo, a site map, examples of photos we might use and very rough draft of the website copy.

Target Market(s)

The customers will mostly be seniors. But, the people who will decide to use the company will the the 50 year old children of those seniors. Also, it is mostly women who are looking for help for their parents.

Industry/Entity Type

It Company

Number of Pages Required

5+ page

Requirements
Nice to have
• I want site visitors to easily be able to contact us with a phone call or through the website. The home page should inspire people to call us.

```html
<!DOCTYPE html>
<html lang="en">
<head>
<meta charset="utf-8">
<title>Larkmoor Home Care</title>
<link href="https://fonts.googleapis.com/css2?family=Cinzel:wght@400;600&family=Lato:ital,wght@0,400;0,700;1,400&display=swap" rel="stylesheet">
<style>
:root{
  --blue:#1a7fcf;
  --blue-dark:#0f68b3;
  --ink:#2a2a2a;
  --text:#444;
  --muted:#777;
  --line:#cfcfcf;
  --pale:#efefef;
  --footer:#262626;
  --footer-text:#cfcfcf;
  --icon-dark:#333;
}
*{box-sizing:border-box;margin:0;padding:0}
html,body{width:1200px;height:3077px;overflow:hidden}
body{position:relative;font-family:"Lato",sans-serif;color:var(--text);background:#fff;font-size:13px}
.abs{position:absolute}
.heading{font-family:"Cinzel",serif;font-weight:400;font-size:32px;color:var(--ink);letter-spacing:1px}
.heading span{color:var(--blue)}
.divider{position:absolute;height:1px;background:var(--line)}
.btn{position:absolute;background:var(--blue);color:#fff;font-weight:700;font-size:13px;display:flex;align-items:center;justify-content:center;letter-spacing:.5px}

/* header */
.header{top:0;left:0;width:1200px;height:115px;background:#fff;border-top:4px solid #2c2c2c}
.logo{left:98px;top:36px;display:flex;align-items:center;gap:12px;font-family:"Cinzel",serif;font-weight:600;font-size:30px;color:var(--blue)}
.logo b{display:block;width:16px;height:16px;background:var(--blue)}
.phone-tab{top:0;left:895px;width:195px;height:30px;background:#2c2c2c;color:#fff;border-radius:0 0 0 16px;display:flex;align-items:center;justify-content:center;gap:8px;font-size:16px;letter-spacing:1px}
.search{top:60px;left:878px;width:222px;height:30px;border:1px solid #d8d8d8;font-size:11px;color:#999;padding:0 12px;display:flex;align-items:center;justify-content:space-between}
.nav{top:115px;left:0;width:1200px;height:40px;background:linear-gradient(#2a8fdb,var(--blue-dark))}
.nav ul{list-style:none;position:absolute;left:98px;width:1002px;height:40px;display:flex;justify-content:space-between;align-items:center}
.nav li{color:#fff;font-size:13px;padding:0 22px;height:40px;display:flex;align-items:center}
.nav li.active{background:#4aa6ea;font-weight:700}

/* hero */
.hero{top:155px;left:0;width:1200px;height:513px;background:linear-gradient(100deg,#d9d2c7 0%,#b9b2a6 35%,#8f9aa0 60%,#c6b7a6 100%)}
.hero-title{left:102px;top:335px;font-size:34px;color:#222;font-weight:700;letter-spacing:.5px}
.hero-tag{left:102px;top:392px;font-size:19px;color:#222}
.hero .dots{position:absolute;left:566px;top:470px;display:flex;gap:6px}
.hero .dots i{width:11px;height:11px;border:2px solid #fff;border-radius:50%}

/* about */
.about-sub{left:98px;top:800px;color:var(--blue);font-weight:700;font-size:14px}
.about-copy{left:98px;top:832px;width:600px;font-size:13px;line-height:21px;color:#333}

/* services */
.services{top:1040px;left:0;width:1200px;height:500px;background:linear-gradient(90deg,#e6e2de,#f2efec 40%,#e3ddd6 70%,#ebe7e2)}
.services .intro{position:absolute;left:120px;width:960px;top:133px;text-align:center;font-size:12.5px;line-height:21px;color:#333}
.service{position:absolute;top:205px;width:230px;text-align:center;color:var(--icon-dark)}
.service.on{color:var(--blue)}
.service .icon{display:block;width:150px;height:140px;margin:0 auto}
.service h3{font-family:"Cinzel",serif;font-weight:400;font-size:16px;color:#222;margin-top:16px;letter-spacing:1px}
.service.on h3{color:var(--blue)}
.service p{font-size:12px;line-height:18px;color:#333;height:36px;overflow:hidden;margin-top:4px}
.service .plus{width:22px;height:22px;margin:16px auto 0;background:#2a2a2a;color:#fff;font-weight:700;display:flex;align-items:center;justify-content:center;font-size:16px}
.service.on .plus{background:var(--blue)}
.arrow{position:absolute;color:#999;font-size:30px}

/* why */
.why{top:1540px;left:0;width:1200px;height:390px;background:var(--pale)}
.why .area{position:absolute;left:98px;top:130px;width:660px;font-size:13px;line-height:21px;color:#333}
.checks{position:absolute;top:198px;list-style:none}
.checks li{height:32px;display:flex;align-items:center;gap:12px;font-size:13px;color:#333}
.checks svg{flex:none}

/* news */
.news-item{position:absolute;left:98px;width:462px;height:70px}
.date{position:absolute;left:0;top:0;width:62px;height:62px;border:1px solid #ccc;text-align:center;background:#fff}
.date b{display:block;background:var(--blue);color:#fff;font-size:12px;height:24px;line-height:24px}
.date span{display:block;font-size:18px;line-height:36px;color:#222}
.news-item h4{position:absolute;left:68px;top:0;font-size:12.5px;font-weight:700;color:#222}
.news-item p{position:absolute;left:68px;top:20px;width:400px;font-size:11.5px;line-height:16px;color:#555}
.faq{position:absolute;left:638px;width:462px;height:34px;background:#e6e6e6;font-size:12.5px;font-weight:700;color:#333;display:flex;align-items:center;padding:0 10px;justify-content:space-between}
.faq i{width:16px;height:16px;border-radius:50%;background:#444;color:#fff;font-style:normal;font-size:13px;display:flex;align-items:center;justify-content:center}
.faq.open{background:var(--blue);color:#fff}
.faq.open i{background:#fff;color:var(--blue)}
.faq-answer{position:absolute;left:638px;top:2234px;width:462px;height:64px;border:1px solid var(--blue);border-top:0;padding:12px 16px;font-size:11.5px;line-height:17px;color:#333}

/* reviews */
.reviews{top:2340px;left:0;width:1200px;height:385px;background:#ececec}
.avatar{position:absolute;top:150px;width:86px;height:86px;border-radius:50%;border:4px solid #fff;box-shadow:0 0 0 1px #ccc}
.avatar.on{box-shadow:0 0 0 3px var(--blue)}
.quote{position:absolute;left:140px;width:920px;top:260px;text-align:center;font-style:italic;font-size:12.5px;line-height:27px;color:#555}
.quote b{color:#9dc8ee;font-size:40px;font-style:normal;line-height:0;vertical-align:-14px;font-family:Georgia,serif}

/* footer */
.footer{top:2725px;left:0;width:1200px;height:305px;background:var(--footer);color:var(--footer-text)}
.footer h5{position:absolute;top:48px;font-family:"Cinzel",serif;font-weight:400;font-size:16px;color:#fff;letter-spacing:1px;padding-bottom:10px;border-bottom:1px solid #444;width:150px}
.links{position:absolute;left:100px;top:90px;list-style:none;font-size:12px;line-height:23px}
.links li::before{content:"› ";color:#999}
.contact{position:absolute;left:312px;top:90px;font-size:13px;line-height:20px}
.contact div{display:flex;gap:10px;margin-bottom:16px}
.field{position:absolute;left:612px;width:273px;background:#fff;color:#666;font-size:12px;padding:8px 10px}
.footer-logo{position:absolute;left:930px;top:205px;font-family:"Cinzel",serif;font-weight:400;font-size:26px;color:#888;display:flex;align-items:center;gap:10px}
.footer-logo b{width:14px;height:14px;background:#888;display:block}
.bottom{top:3030px;left:0;width:1200px;height:47px;background:var(--blue-dark);color:#fff;font-size:12px;display:flex;align-items:center;justify-content:center}
</style>
</head>
<body>

<header class="abs header">
  <div class="abs logo"><b></b>Larkmoor Home Care</div>
  <div class="abs phone-tab">
    <svg width="14" height="14" viewBox="0 0 24 24"><path fill="#fff" d="M6.6 10.8a15 15 0 0 0 6.6 6.6l2.2-2.2c.3-.3.7-.4 1-.2 1.1.4 2.3.6 3.6.6.6 0 1 .4 1 1V20c0 .6-.4 1-1 1A17 17 0 0 1 3 4c0-.6.4-1 1-1h3.5c.6 0 1 .4 1 1 0 1.3.2 2.5.6 3.6.1.3 0 .7-.2 1z"/></svg>
    555.014.2290
  </div>
  <div class="abs search">Search
    <svg width="12" height="12" viewBox="0 0 24 24"><circle cx="10" cy="10" r="7" fill="none" stroke="#999" stroke-width="2"/><path d="M15 15l6 6" stroke="#999" stroke-width="2"/></svg>
  </div>
</header>

<nav class="abs nav">
  <ul>
    <li class="active">Home</li><li>About Us</li><li>Services</li><li>Free In-Home Consultation</li><li>News</li><li>Reviews</li><li>FAQ</li><li>Client Portal</li><li>Contact Us</li>
  </ul>
</nav>

<section class="abs hero" role="img" aria-label="Photo of a smiling caregiver handing a glass of water to an elderly woman">
  <div class="dots"><i></i><i></i><i></i><i></i></div>
</section>
<h1 class="abs hero-title">Larkmoor Home Care</h1>
<p class="abs hero-tag">Family-Owned, Service You Can Trust</p>
<div class="btn" style="left:98px;top:428px;width:156px;height:46px;font-size:14px">CONTACT NOW</div>

<h2 class="abs heading" style="left:98px;top:705px">About <span>Us</span></h2>
<div class="divider" style="left:98px;top:767px;width:582px"></div>
<p class="abs about-sub">The Reason We Started Larkmoor Home Care Is Simple</p>
<p class="abs about-copy">we love people. We've experienced home care before and knew we can do it better. My husband and I know the process can be confusing, time consuming and stressful, but it shouldn't be. We decided to do our part by making everything as simple, safe and easy as possible. Often times, when you're searching and call a home care company, you'll find out later you've reached a referral service or registry, not an actual home care provider.</p>
<div class="btn" style="left:98px;top:964px;width:130px;height:34px">READ MORE</div>
<div class="abs" style="left:723px;top:718px;width:372px;height:280px;background:linear-gradient(135deg,#6f8a5e,#b7a58e 55%,#5d7a4f);border:4px solid #fff;box-shadow:0 0 0 1px #ddd" role="img" aria-label="Photo of a caregiver in green scrubs sitting with a smiling senior woman outdoors"></div>

<section class="abs services" role="img" aria-label="Soft faded photo of a caregiver holding a senior's hands">
  <h2 class="heading" style="position:absolute;left:0;width:1200px;text-align:center;top:37px">Our <span>Services</span></h2>
  <div class="divider" style="left:408px;top:95px;width:384px"></div>
  <p class="intro">Larkmoor Home Care offers a wide variety of home care services, from once a week visits to 24-hour care. Since every situation is unique, we work together with you to create the perfect program.</p>
  <span class="arrow" style="left:62px;top:230px">‹</span>
  <span class="arrow" style="left:1118px;top:230px">›</span>
  <div class="service on" style="left:100px">
    <svg class="icon" viewBox="0 0 150 140" role="img" aria-label="Companionship icon"><circle cx="75" cy="70" r="62" fill="none" stroke="currentColor" stroke-width="7"/><circle cx="75" cy="70" r="40" fill="currentColor" opacity=".18"/></svg>
    <h3>Companionship</h3><p>Our goal is to keep your loved one active and engaged mentally and socially every day.</p><div class="plus">+</div></div>
  <div class="service" style="left:355px">
    <svg class="icon" viewBox="0 0 150 140" role="img" aria-label="Personal care icon"><circle cx="75" cy="70" r="62" fill="none" stroke="currentColor" stroke-width="7"/><circle cx="75" cy="70" r="40" fill="currentColor" opacity=".18"/></svg>
    <h3>Personal Care</h3><p>Our caretakers can offer a helping hand for dressing, bathing, or using the bathroom.</p><div class="plus">+</div></div>
  <div class="service" style="left:612px">
    <svg class="icon" viewBox="0 0 150 140" role="img" aria-label="Housekeeping icon"><circle cx="75" cy="70" r="62" fill="none" stroke="currentColor" stroke-width="7"/><circle cx="75" cy="70" r="40" fill="currentColor" opacity=".18"/></svg>
    <h3>Housekeeping</h3><p>Having a clean living space is essential for maintaining optimal health.</p><div class="plus">+</div></div>
  <div class="service" style="left:870px">
    <svg class="icon" viewBox="0 0 150 140" role="img" aria-label="Transportation icon"><circle cx="75" cy="70" r="62" fill="none" stroke="currentColor" stroke-width="7"/><circle cx="75" cy="70" r="40" fill="currentColor" opacity=".18"/></svg>
    <h3>Transportation</h3><p>Let us take the wheel, driving your loved one to appointments, running errands.</p><div class="plus">+</div></div>
</section>

<section class="abs why">
  <h2 class="heading" style="position:absolute;left:0;width:1200px;text-align:center;top:33px">Why <span>Choose Us</span></h2>
  <div class="divider" style="left:408px;top:90px;width:384px"></div>
  <p class="area">Serving the Inland Empire including Chino, Chino Hills, Corona, Eastvale, Jurupa Valley, Norco, Moreno Valley, Ontario, Rancho Cucamonga, Riverside, Redlands, San Bernardino and all other inland communities.</p>
  <ul class="checks" style="left:98px">
    <li><svg width="16" height="16" viewBox="0 0 16 16"><rect x="1" y="3" width="12" height="12" fill="#fff" stroke="#555"/><path d="M3 8l3 3 8-9" fill="none" stroke="#333" stroke-width="2"/></svg>Family Owned</li>
    <li><svg width="16" height="16" viewBox="0 0 16 16"><rect x="1" y="3" width="12" height="12" fill="#fff" stroke="#555"/><path d="M3 8l3 3 8-9" fill="none" stroke="#333" stroke-width="2"/></svg>Insured</li>
    <li><svg width="16" height="16" viewBox="0 0 16 16"><rect x="1" y="3" width="12" height="12" fill="#fff" stroke="#555"/><path d="M3 8l3 3 8-9" fill="none" stroke="#333" stroke-width="2"/></svg>All employees pre-screened</li>
    <li><svg width="16" height="16" viewBox="0 0 16 16"><rect x="1" y="3" width="12" height="12" fill="#fff" stroke="#555"/><path d="M3 8l3 3 8-9" fill="none" stroke="#333" stroke-width="2"/></svg>Detailed written care plan</li>
    <li><svg width="16" height="16" viewBox="0 0 16 16"><rect x="1" y="3" width="12" height="12" fill="#fff" stroke="#555"/><path d="M3 8l3 3 8-9" fill="none" stroke="#333" stroke-width="2"/></svg>Licensed/Bonded</li>
  </ul>
  <ul class="checks" style="left:372px">
    <li><svg width="16" height="16" viewBox="0 0 16 16"><rect x="1" y="3" width="12" height="12" fill="#fff" stroke="#555"/><path d="M3 8l3 3 8-9" fill="none" stroke="#333" stroke-width="2"/></svg>Agency, not Registry</li>
    <li><svg width="16" height="16" viewBox="0 0 16 16"><rect x="1" y="3" width="12" height="12" fill="#fff" stroke="#555"/><path d="M3 8l3 3 8-9" fill="none" stroke="#333" stroke-width="2"/></svg>Worker's comp insurance included</li>
    <li><svg width="16" height="16" viewBox="0 0 16 16"><rect x="1" y="3" width="12" height="12" fill="#fff" stroke="#555"/><path d="M3 8l3 3 8-9" fill="none" stroke="#333" stroke-width="2"/></svg>We listen to your needs and requirements</li>
    <li><svg width="16" height="16" viewBox="0 0 16 16"><rect x="1" y="3" width="12" height="12" fill="#fff" stroke="#555"/><path d="M3 8l3 3 8-9" fill="none" stroke="#333" stroke-width="2"/></svg>Emphasis on mental and physical activity, engagement</li>
  </ul>
  <div style="position:absolute;left:788px;top:135px;width:312px;height:212px;background:linear-gradient(120deg,#7aa3b8,#c98f7f 50%,#5c7d96);border:4px solid #fff;box-shadow:0 0 0 1px #ccc" role="img" aria-label="Photo of a senior man with two family members at home"></div>
</section>

<h2 class="abs heading" style="left:98px;top:1968px">Latest <span>News</span></h2>
<svg class="abs" style="left:524px;top:1987px" width="40" height="16" viewBox="0 0 40 16"><circle cx="8" cy="8" r="6.5" fill="none" stroke="#e88"/><path d="M9.5 5l-3 3 3 3" fill="none" stroke="#e88"/><circle cx="28" cy="8" r="6.5" fill="none" stroke="#3b9"/><path d="M26.5 5l3 3-3 3" fill="none" stroke="#3b9"/></svg>
<div class="divider" style="left:98px;top:2030px;width:462px"></div>
<div class="news-item" style="top:2068px"><div class="date"><b>July</b><span>08</span></div><h4>Sed ut perspiciatis unde omnis iste natus error sit voluptatem</h4><p>Accusant doloremque laudantium, totamrem aperiam, moregi eaquenm ipsa quae ab illoi facilies.</p></div>
<div class="news-item" style="top:2150px"><div class="date"><b>July</b><span>08</span></div><h4>Sed ut perspiciatis unde omnis iste natus error sit voluptatem</h4><p>Accusant doloremque laudantium, totamrem aperiam, moregi eaquenm ipsa quae ab illoi facilies.</p></div>
<div class="news-item" style="top:2232px"><div class="date"><b>July</b><span>08</span></div><h4>Sed ut perspiciatis unde omnis iste natus error sit voluptatem</h4><p>Accusant doloremque laudantium, totamrem aperiam, moregi eaquenm ipsa quae ab illoi facilies.</p></div>

<h2 class="abs heading" style="left:638px;top:1968px">FAQ<span>'s</span></h2>
<div class="divider" style="left:638px;top:2030px;width:462px"></div>
<div class="faq" style="top:2066px">1. Are you licensed and insured?<i>+</i></div>
<div class="faq" style="top:2110px">2. Are there any hidden fees?<i>+</i></div>
<div class="faq" style="top:2154px">3. Are your employees fully vetted?<i>+</i></div>
<div class="faq open" style="top:2200px">4. What if my caregiver cancels?<i>−</i></div>
<div class="faq-answer">On the rare occasion that your caregiver cannot make their appointment, we will send another carefully screened employee in their place.</div>

<section class="abs reviews">
  <h2 class="heading" style="position:absolute;left:0;width:1200px;text-align:center;top:40px">Client <span>Reviews</span></h2>
  <div class="divider" style="left:408px;top:97px;width:384px"></div>
  <span class="arrow" style="left:308px;top:165px;color:#bbb">‹</span>
  <span class="arrow" style="left:872px;top:165px;color:#bbb">›</span>
  <div class="avatar on" style="left:375px;background:#8a7566" role="img" aria-label="Client portrait"></div>
  <div class="avatar" style="left:497px;background:#c79a72" role="img" aria-label="Client portrait"></div>
  <div class="avatar" style="left:617px;background:#b6aca4" role="img" aria-label="Client portrait"></div>
  <div class="avatar" style="left:740px;background:#9a7e6b" role="img" aria-label="Client portrait"></div>
  <p class="quote"><b>“</b> Sed ut perspiciatis unde omnis iste natus error sit voluptatem accusantium doloremque laudantium, totam rem aperiam, eaque ipsa quae ab illo inventore veritatis et quasi architecto beatae vitae dicta sunt explicabo. Nemo enim ipsam voluptatem quia voluptas sit aspernatur aut odit aut fugit, sed quia consequuntur magni dolores eos qui ratione voluptatem sequi nesciunt. Neque porro quisquam est, qui dolorem ipsum quia dolor sit amet <b>”</b></p>
</section>

<footer class="abs footer">
  <h5 style="left:100px">Quick Links</h5>
  <ul class="links">
    <li>Home</li><li>About Us</li><li>Services</li><li>Free In-Home Consultation</li><li>News</li><li>FAQ</li><li>Client Portal</li><li>Contact Us</li>
  </ul>
  <h5 style="left:312px;width:230px">Contact Detail</h5>
  <div class="contact">
    <div><svg width="12" height="16" viewBox="0 0 12 16"><path d="M6 0a6 6 0 0 0-6 6c0 4 6 10 6 10s6-6 6-10a6 6 0 0 0-6-6z" fill="#ccc"/><circle cx="6" cy="6" r="2" fill="#262626"/></svg><span><b style="color:#fff">Larkmoor Home Care</b><br>48 Fernhollow Lane, Suite 2,<br>Brookvale Road.</span></div>
    <div><svg width="14" height="14" viewBox="0 0 24 24"><path fill="#ccc" d="M6.6 10.8a15 15 0 0 0 6.6 6.6l2.2-2.2c.3-.3.7-.4 1-.2 1.1.4 2.3.6 3.6.6.6 0 1 .4 1 1V20c0 .6-.4 1-1 1A17 17 0 0 1 3 4c0-.6.4-1 1-1h3.5c.6 0 1 .4 1 1 0 1.3.2 2.5.6 3.6.1.3 0 .7-.2 1z"/></svg>555 014 2290</div>
    <div><svg width="14" height="14" viewBox="0 0 14 14"><rect x="3" y="1" width="8" height="4" fill="#ccc"/><rect x="1" y="5" width="12" height="6" fill="#ccc"/><rect x="3" y="9" width="8" height="4" fill="#888"/></svg>555 014 2290</div>
    <div><svg width="14" height="12" viewBox="0 0 14 12"><rect x="0" y="1" width="14" height="10" fill="#ccc"/><path d="M0 1l7 5 7-5" fill="none" stroke="#262626"/></svg>info@larkmoorhomecare.com</div>
  </div>
  <h5 style="left:612px;width:273px">Quick Contact</h5>
  <div class="field" style="top:90px;height:34px">Name</div>
  <div class="field" style="top:132px;height:34px">Email</div>
  <div class="field" style="top:175px;height:50px">Message</div>
  <div class="btn" style="left:612px;top:232px;width:118px;height:34px">SUBMIT</div>
  <div class="footer-logo"><b></b>Larkmoor<br>Home Care</div>
</footer>
<div class="abs bottom">© 2016 Larkmoor Home Care. All Rights Reserved.</div>

</body>
</html>
```